Book cover for "Generous Horizons" encouraging business to take up compassion pr...

I need a book cover designed for "Generous Horizons. Where Winning Falls Short." The book encourages businesses to take up a social mission (that is, to have a social impact, such as corporate social responsibility.) in doing so, they find a greater sense of purpose, their employees and the community are more engaged, and their business grows. I use stories from my podcast Civic Purpose Uprising. 2 key word/phrases that may help t think about are Philanthropy and Corporate Social Responsibility.
This book will be followed by 1 or 2 other books. Another seies of books will also soon requre work.

The market is Mid-sized business owners and CEOs. They have built up the business to a successful place but now find that doesn't bring fulfilment or happiness. The cover needs to have a business or corporate feel.
The Colouring of the book, focus on blues and purples.
This will be a thin book - a quick and easy read of around 110 pages. It is 5x8 inches.
I would be happy to have a photo of me incorporated, but not the focus. I could have a photo done as directed by the designer, as I am planning to have a photoshoot done soon.
Fonts - Please chose a font with the rounded "a", such as in the Century Gothic font, however, open to suggestions.
The back cover will include:
o A book blurb – still to be written
o 2 or 3 endorsements
o Publishing logo (as it is my own publishing company.
o ISBN and barcode
On the spine
• Generous Horizons
• Belinda Morcombe
• Publisher logo icon

For your interest: Belinda is a Speaker, Author, podcaster and Trusted Advisor to Authentic Influencers. Through nourishing community, Belinda maximises the potential of business and influences change.

Target Market(s)

The market is Mid-sized business owners and CEOs. They have built up the business to a successful place but now find that doesn't bring fulfillment or happiness. The cover needs to have a business or corporate feel.

Industry/Entity Type

This is business/corporate book

Font styles to use
Other font styles liked:
• Please chose a font with the rounded "a", such as in the Century Gothic font, however, open to suggestions.

Colors
0054AA
0677BA
7BADD7
CADEEF
E8F1F8
A7469A
B969AE
D3A5CF
EDDBEB
F8F0F9
6B429C
8869AF
B7A5CE
E3DAEB
F3F0F8

Requirements
Must have
• An eye catching design with a business feel.
Nice to have
• I would be nice to edit me into the cover somehow - like Lindqvist puts himself in the background of his movies. I can have photos taken to match .

```html
<!DOCTYPE html>
<html lang="en">
<head>
<meta charset="utf-8">
<title>Generous Horizons — Book Cover</title>
<link rel="stylesheet" href="https://fonts.googleapis.com/css2?family=Big+Shoulders+Inline+Display:wght@800&family=Cinzel:wght@700;900&display=swap">
<style>
  :root {
    --backdrop: #9bd4c2;
    --cover-white: #ffffff;
    --brand-yellow: #f8d53b;
    --brand-blue: #17409a;
    --emblem-blue: #3f62ad;
    --emblem-yellow: #f3df86;
    --text-white: #ffffff;
  }
  html, body {
    margin: 0;
    padding: 0;
    width: 1200px;
    height: 857px;
    overflow: hidden;
    background: var(--backdrop);
  }
  .canvas {
    position: relative;
    width: 1200px;
    height: 857px;
  }
  .book-cover {
    position: absolute;
    left: 334px;
    top: 38px;
    width: 532px;
    height: 780px;
    display: block;
  }
  .title-main {
    font-family: "Big Shoulders Inline Display", "Impact", sans-serif;
    font-weight: 800;
    font-size: 74px;
    letter-spacing: 6px;
    fill: var(--brand-blue);
  }
  .title-sub {
    font-family: "Cinzel", "Times New Roman", serif;
    font-weight: 900;
    font-size: 28px;
    fill: var(--brand-yellow);
  }
  .subtitle-lead {
    font-family: "Cinzel", "Times New Roman", serif;
    font-weight: 900;
    font-size: 31px;
    fill: var(--text-white);
  }
  .subtitle-link {
    font-family: "Cinzel", "Times New Roman", serif;
    font-weight: 900;
    font-size: 16px;
    fill: var(--text-white);
  }
  .subtitle-close {
    font-family: "Big Shoulders Inline Display", "Impact", sans-serif;
    font-weight: 800;
    font-size: 62px;
    letter-spacing: 6px;
    fill: var(--brand-yellow);
  }
  .author-name {
    font-family: "Cinzel", "Times New Roman", serif;
    font-weight: 900;
    font-size: 29px;
    fill: var(--brand-blue);
  }
</style>
</head>
<body>
<main class="canvas">
  <svg class="book-cover" viewBox="0 0 532 780" xmlns="http://www.w3.org/2000/svg" aria-label="Generous Horizons book cover">
    <defs>
      <radialGradient id="emblem-tone" cx="0.5" cy="0.5" r="0.6">
        <stop offset="0" stop-color="var(--emblem-blue)"/>
        <stop offset="1" stop-color="var(--emblem-yellow)"/>
      </radialGradient>
    </defs>

    <rect class="cover-surface" x="0" y="0" width="532" height="780" fill="var(--cover-white)"/>

    <g class="title-block">
      <rect x="42" y="27" width="446" height="84" fill="var(--brand-yellow)"/>
      <text class="title-main" x="265" y="100" text-anchor="middle">GENEROUS</text>
      <rect x="42" y="111" width="446" height="33" fill="var(--brand-blue)"/>
      <text class="title-sub" x="265" y="138" text-anchor="middle" textLength="380" lengthAdjust="spacing">HORIZONS</text>
    </g>

    <g class="cover-emblem" role="img" aria-label="Central emblem artwork in blue and yellow">
      <rect x="123" y="188" width="308" height="287" rx="12" fill="url(#emblem-tone)"/>
    </g>

    <g class="subtitle-block">
      <rect x="42" y="505" width="446" height="139" fill="var(--brand-blue)"/>
      <text class="subtitle-lead" x="265" y="545" text-anchor="middle" textLength="280" lengthAdjust="spacingAndGlyphs">WHERE WINNING</text>
      <line x1="124" y1="563" x2="230" y2="563" stroke="var(--text-white)" stroke-width="2.5"/>
      <text class="subtitle-link" x="265" y="569" text-anchor="middle">FALLS</text>
      <line x1="300" y1="563" x2="406" y2="563" stroke="var(--text-white)" stroke-width="2.5"/>
      <text class="subtitle-close" x="265" y="628" text-anchor="middle">SHORT</text>
    </g>

    <g class="author-block">
      <rect x="42" y="692" width="446" height="59" fill="var(--brand-yellow)"/>
      <text class="author-name" x="265" y="733" text-anchor="middle" textLength="412" lengthAdjust="spacingAndGlyphs">BELINDA MORCOMBE</text>
    </g>
  </svg>
</main>
</body>
</html>
```